731 Orchard Avenue Residences

designing a sign for apartment complex;
prefer colors gray white and yellow

Target Market(s)

residents coming home to their apartment

Font styles to use
Serif
Sans Serif

Colors
FFF300
FFF600
FEFA6F
FFFEC7
FFFEE8

Requirements
Must have
• black or gray, white and some yellow; easy to read and see

```html
<!DOCTYPE html>
<html lang="en">
<head>
<meta charset="utf-8">
<title>731 Orchard Avenue Residences – Entrance Sign</title>
<link rel="stylesheet" href="https://fonts.googleapis.com/css2?family=Cinzel:wght@700&display=swap">
<style>
  :root {
    --page: #ffffff;
    --frame-gray: #afb0af;
    --accent-yellow: #fff300;
    --panel-black: #000000;
    --line-white: #ffffff;
    --lettering: #ffffff;
  }
  html, body {
    margin: 0;
    padding: 0;
    width: 1200px;
    height: 1200px;
    overflow: hidden;
    background: var(--page);
  }
  .sign-canvas {
    display: block;
    width: 1200px;
    height: 1200px;
  }
  .plaque {
    filter: drop-shadow(0 22px 18px rgba(0, 0, 0, 0.38));
  }
  .plaque-base { fill: var(--panel-black); }
  .band-yellow { fill: none; stroke: var(--accent-yellow); stroke-width: 96; }
  .band-gray { fill: none; stroke: var(--frame-gray); stroke-width: 56; }
  .inner-rule-white { fill: none; stroke: var(--line-white); stroke-width: 132; }
  .inner-rule-black { fill: none; stroke: var(--panel-black); stroke-width: 124; }
  .crest-ornament { fill: var(--accent-yellow); }
  .sign-text {
    font-family: "Cinzel", "Times New Roman", serif;
    font-weight: 700;
    fill: var(--lettering);
    text-anchor: middle;
  }
  .street-number { font-size: 100px; letter-spacing: 2px; }
  .street-name { font-size: 96px; }
</style>
</head>
<body>
<svg class="sign-canvas" viewBox="0 0 1500 1500" xmlns="http://www.w3.org/2000/svg" role="img" aria-label="731 Orchard Avenue Residences sign">
  <defs>
    <path id="plaque-outline" d="M 525 440 C 590 318 910 318 975 440 L 1150 440 Q 1175 530 1245 545 L 1245 620 Q 1355 620 1355 750 Q 1355 880 1245 880 L 1245 955 Q 1175 970 1150 1060 L 975 1060 C 910 1182 590 1182 525 1060 L 350 1060 Q 325 970 255 955 L 255 880 Q 145 880 145 750 Q 145 620 255 620 L 255 545 Q 325 530 350 440 Z"/>
    <clipPath id="plaque-clip">
      <use href="#plaque-outline"/>
    </clipPath>
  </defs>

  <g class="plaque">
    <use href="#plaque-outline" class="plaque-base"/>
    <g clip-path="url(#plaque-clip)">
      <use href="#plaque-outline" class="inner-rule-white"/>
      <use href="#plaque-outline" class="inner-rule-black"/>
      <use href="#plaque-outline" class="band-yellow"/>
      <use href="#plaque-outline" class="band-gray"/>
    </g>
  </g>

  <rect class="crest-ornament" x="708" y="432" width="84" height="112" rx="34" role="img" aria-label="Yellow fleur-de-lis crest ornament"/>

  <text class="sign-text street-number" x="750" y="640">731</text>
  <text class="sign-text street-name" x="750" y="742">Orchard</text>
  <text class="sign-text street-name" x="750" y="846">Avenue</text>
  <text class="sign-text street-name" x="750" y="948">Residences</text>
</svg>
</body>
</html>
```